Wine Shop Banners

Banner graphic/images required
Require banner images to match the present online wine shop.

www.kelterhaus-traube.de

The wine-shop presently has a very clean, simple design, lots of white space, which is very much the trend at the moment.

Requirements
Images or graphic design for present banners visible on the homepage

The colour and feeling of the banners must fit in with the present clean, simple design.

Work required
3 large slide-card/banners (can be more) and 3 smaller fixed banners below. Please view website to see present position of banners.

LARGE BANNERS x 3

Something special with white background within the banner space
White background on each slide-card. Small individual graphic image in the middle of the slide card. This could be either a simple element of wine:
ingredients, fruit (grape), bottle, cork, old bottle label etc. just displaying one item on each slide-card. Preferably with high quality graphic features.

Note:
We are trying the steer away from the classic stereotype wineshop design. The image/s should have a higher, individual graphic touch, which gives the design something different. Sometimes such artistic work is displayed in steampunk or even in nostalgic design, which leaves the viewer slightly memorized with the content.
To clarify: we are not looking for a full steampunk design but possibly certain elements of this will give you an idea what we mean. That is to say, the design can go slightly in this direction without going over the top. Something small but very eye-catching.

SMALLER BANNERS x 3

One idea is:
Showing a symbol e.g. - discount sign "%" against a white background but again with a high graphic quality.

Target Market(s)

People interested in purchasing wine.
Ages approx. 25 to 65

Industry/Entity Type

Shop

Requirements
Must have
• Something special with white background
• Small individual graphic image in the middle of the slide card.
Nice to have
• The image/s should have a higher, individual graphic touch, which gives the design something different. Something that leaves the viewer slightly memorized with the content.
Should not have
• Not the typical classical design that is often seen on wine shops.

```html
<!DOCTYPE html>
<html lang="en">
<head>
<meta charset="utf-8">
<title>Kelterhaus Traube – Wine Shop</title>
<link rel="stylesheet" href="https://fonts.googleapis.com/css2?family=Open+Sans:wght@400;600&family=Marcellus&family=Merriweather&display=swap">
<style>
:root{
  --olive:#5b5d35;
  --wine:#a8204a;
  --lime:#cfdc63;
  --lime-text:#c3d15a;
  --badge:#b6b91f;
  --ink:#3a3a3a;
  --muted:#8a8a8a;
  --line:#d9d9d9;
  --bg:#ffffff;
}
*{box-sizing:border-box;margin:0;padding:0}
html,body{width:1200px;height:906px;overflow:hidden;background:var(--bg)}
body{position:relative;font-family:"Open Sans",Arial,sans-serif;color:var(--ink)}
.abs{position:absolute}
.top-rule{left:0;top:0;width:1200px;height:1px;background:var(--line)}

/* header */
.brand{left:76px;top:30px;font-family:"Marcellus",Georgia,serif;color:var(--olive);line-height:1}
.brand .name{font-size:33px;letter-spacing:1px}
.brand .sub{font-size:14px;letter-spacing:5px;margin-top:12px}
.search{left:589px;top:37px;width:287px;height:32px;border:1px solid #555;display:flex;align-items:center}
.search svg{margin:0 12px 0 10px}
.search span{font-size:13px;color:#666;flex:1}
.search .go{width:42px;height:100%;background:var(--wine);color:#fff;font-weight:600;font-size:15px;display:flex;align-items:center;justify-content:center}
.account{left:989px;top:24px;display:flex;align-items:center;gap:12px;font-size:16px;color:#555}
.nav{left:92px;top:116px;font-size:16.5px;color:#444}
.nav span{position:absolute;white-space:nowrap}
.icon-badge{width:18px;height:18px;border-radius:50%;background:var(--badge);color:#fff;font-size:11px;display:flex;align-items:center;justify-content:center}

/* sidebar */
.filter-head{left:75px;top:155px;width:214px;height:36px;background:var(--lime);font-weight:600;font-size:14.5px;color:#444;padding:8px 12px}
.group-title{left:76px;font-size:15px;color:var(--lime-text);letter-spacing:.2px}
.list{left:76px;list-style:none;font-size:14.5px}
.list li{height:23px;line-height:23px;white-space:nowrap}
.list li::before{content:"›";margin-right:7px;color:#555}
.list em{font-style:normal;color:var(--muted)}
.country-box{left:76px;top:232px;width:190px;height:166px;overflow:hidden}
.scrollbar{left:269px;top:232px;width:16px;height:166px;background:#f1f1f1}
.scrollbar i{position:absolute;left:2px;top:18px;width:12px;height:66px;background:#c1c1c1}
.price-track{left:82px;top:778px;width:190px;height:4px;border:1px solid #bbb;border-radius:2px}
.price-knob{top:773px;width:11px;height:13px;border:1px solid #999;border-radius:4px;background:#fff}
.price-label{left:82px;top:789px;width:190px;text-align:center;font-size:13px}
.region-input{left:77px;top:861px;width:208px;height:39px;border:1px solid #ccc;font-size:13px;color:#777;padding:11px 12px}

/* hero */
.hero{left:300px;top:155px;width:797px;height:310px;border:1px solid #ddd;background:radial-gradient(ellipse at 60% 50%,#fafafa,#e2e2e2);overflow:hidden}
.hero-art{left:330px;top:10px;width:460px;height:290px;background:
  radial-gradient(ellipse 30% 32% at 82% 38%,rgba(140,190,70,.35),transparent 100%),
  radial-gradient(ellipse 48% 46% at 52% 55%,rgba(112,82,150,.55),rgba(112,82,150,.18) 65%,transparent 100%)}
.hero-copy{left:34px;top:170px;width:300px;text-align:center;font-family:"Marcellus",Georgia,serif}
.hero-copy .royal{color:var(--wine);font-size:29px;letter-spacing:1px}
.hero-copy .title{font-size:42px;color:#444;line-height:1}
.hero-copy .cta{display:flex;align-items:center;gap:10px;color:var(--wine);font-size:20px;margin-top:6px}
.hero-copy .cta i{flex:1;height:1px;background:#555}

/* promo tiles */
.promo{top:476px;width:258px;height:120px;border:1px solid #e2e2e2;background:linear-gradient(135deg,#fbfaf7,#efece6);font-family:"Marcellus",Georgia,serif;text-align:center;overflow:hidden}
.promo .txt{position:absolute;left:0;right:0}
.promo-shipping .txt{top:18px;left:8px;width:160px;font-size:21px;line-height:28px;color:#8d8d8d}
.burst{right:0;top:40px}
.promo-anniv .txt{top:27px;font-size:18px;line-height:24px;color:var(--wine)}
.promo-special .txt{top:26px;left:-20px;font-size:26px;line-height:31px;color:var(--wine)}
.promo-special .off{position:absolute;right:6px;bottom:18px;transform:rotate(-45deg);color:var(--badge);font-size:22px;line-height:20px}

/* products */
.section-title{left:299px;top:618px;display:flex;align-items:center;gap:9px;font-family:"Merriweather",Georgia,serif;font-size:15px;color:#222}
.pager{top:619px;width:18px;height:19px;border:1px solid #555;display:flex;align-items:center;justify-content:center}
.section-rule{left:300px;top:646px;width:797px;height:4px;background:#f0f0f0}
.card{top:652px;width:198px;height:254px;border:1px solid #e6e6e6}
.bottle{position:absolute;left:50%;top:14px;width:42px;height:182px;margin-left:-21px;border-radius:10px 10px 4px 4px}
.card p{position:absolute;left:6px;right:6px;top:210px;text-align:center;font-size:13px;line-height:16.5px;color:#444}
</style>
</head>
<body>
<div class="abs top-rule"></div>

<header>
  <div class="abs brand"><div class="name">KELTERHAUS</div><div class="sub">TRAUBE</div></div>
  <div class="abs search">
    <svg width="12" height="12" viewBox="0 0 12 12"><circle cx="5" cy="5" r="3.6" fill="none" stroke="#a8204a" stroke-width="1.8"/><line x1="7.6" y1="7.6" x2="11" y2="11" stroke="#a8204a" stroke-width="2"/></svg>
    <span>Suche</span><div class="go">GO</div>
  </div>
  <div class="abs account">Sign out
    <svg width="26" height="28" viewBox="0 0 26 28"><circle cx="13" cy="9" r="6" fill="none" stroke="#555" stroke-width="2"/><path d="M2 26c0-6 5-10 11-10s11 4 11 10z" fill="none" stroke="#555" stroke-width="2"/></svg>
  </div>
  <nav class="abs nav">
    <span style="left:0">red wine</span><span style="left:103px">White wine</span><span style="left:226px">rose wine</span><span style="left:338px">Champagne / champagne</span><span style="left:574px">Special offers</span><span style="left:715px">Tasting packages</span>
  </nav>
  <svg class="abs" style="left:1008px;top:110px" width="30" height="28" viewBox="0 0 30 28"><path d="M1 3h5l4 15h14l3-10H8" fill="none" stroke="#555" stroke-width="2"/><circle cx="12" cy="24" r="2" fill="#555"/><circle cx="22" cy="24" r="2" fill="#555"/></svg>
  <div class="abs icon-badge" style="left:1022px;top:104px">0</div>
  <svg class="abs" style="left:1061px;top:108px" width="31" height="31" viewBox="0 0 31 31"><circle cx="15.5" cy="15.5" r="15.5" fill="#8c8c8c"/><path d="M15.5 22l-6-6a3.4 3.4 0 0 1 6-4 3.4 3.4 0 0 1 6 4z" fill="none" stroke="#fff" stroke-width="1.6"/></svg>
  <div class="abs icon-badge" style="left:1080px;top:104px">0</div>
</header>

<aside>
  <div class="abs filter-head">DETAILS SEARCH</div>
  <div class="abs group-title" style="top:203px">COUNTRY</div>
  <div class="abs country-box"><ul class="list" style="left:0;position:absolute;top:0">
    <li>Italy <em>(89)</em></li><li>France <em>(74)</em></li><li>Germany <em>(58)</em></li><li>Spain <em>(35)</em></li><li>South Africa <em>(14)</em></li><li>Austria <em>(12)</em></li><li>Australia <em>(12)</em></li><li>Portugal <em>(10)</em></li>
  </ul></div>
  <div class="abs scrollbar"><i></i></div>
  <div class="abs group-title" style="top:419px">TASTE</div>
  <ul class="abs list" style="top:447px"><li>Dry <em>(303)</em></li><li>Half-dry <em>(8th)</em></li><li>Lovely <em>(6)</em></li><li>Sweet <em>(3)</em></li><li>Sweet <em>(1)</em></li></ul>
  <div class="abs group-title" style="top:582px">COLOR</div>
  <ul class="abs list" style="top:611px"><li>red <em>(155)</em></li><li>White <em>(127)</em></li><li>Tingling <em>(23)</em></li><li>Rose <em>(13)</em></li><li>champagne <em>(9)</em></li></ul>
  <div class="abs group-title" style="top:746px">PRICE</div>
  <div class="abs price-track"></div>
  <div class="abs price-knob" style="left:78px"></div><div class="abs price-knob" style="left:265px"></div>
  <div class="abs price-label">2 € - 75 €</div>
  <div class="abs group-title" style="top:826px">REGION</div>
  <div class="abs region-input">Region suchen ...</div>
</aside>

<main>
  <section class="abs hero">
    <div class="abs hero-art" role="img" aria-label="Illustration of a bunch of purple grapes with a green vine leaf and curling tendrils"></div>
    <div class="abs hero-copy">
      <div class="royal">ROYAL</div>
      <div class="title">Quality Wine</div>
      <div class="cta"><i></i>Buy Now<i></i></div>
    </div>
  </section>

  <div class="abs promo promo-shipping" style="left:300px">
    <div class="txt">FREE SHIPPING<br>ON ORDER<br>OVER</div>
    <svg class="abs burst" width="80" height="82" viewBox="0 0 80 82"><polygon fill="#b8194a" points="52,0 58,12 70,6 70,19 80,22 74,32 80,42 72,48 76,60 64,60 62,72 52,68 44,80 38,70 28,76 26,64 14,64 18,52 8,46 16,38 10,28 22,24 20,12 32,14 36,2 44,10"/><text x="46" y="50" text-anchor="middle" fill="#fff" font-family="Marcellus,serif" font-size="28">$25</text></svg>
  </div>
  <div class="abs promo promo-anniv" style="left:568px"><div class="txt">CELEBRATE YOUR<br>ANNIVERSARY WITH<br>TASTE</div></div>
  <div class="abs promo promo-special" style="left:837px"><div class="txt">SPECIALS<br>OFFER</div><div class="off">20%<br>OFF</div></div>

  <div class="abs section-title">
    <svg width="15" height="15" viewBox="0 0 15 15"><circle cx="7.5" cy="7.5" r="6.5" fill="none" stroke="#a8204a" stroke-width="1.2"/><polygon points="6,4.5 10,7.5 6,10.5" fill="#a8204a"/></svg>
    Selected Products
  </div>
  <div class="abs pager" style="left:1055px"><svg width="6" height="9"><polyline points="5,1 1,4.5 5,8" fill="none" stroke="#333"/></svg></div>
  <div class="abs pager" style="left:1077px"><svg width="6" height="9"><polyline points="1,1 5,4.5 1,8" fill="none" stroke="#333"/></svg></div>
  <div class="abs section-rule"></div>

  <article class="abs card" style="left:296px"><div class="bottle" role="img" aria-label="Photo of a rosé sparkling wine bottle" style="background:linear-gradient(90deg,#d99aa2,#f3c7cb,#c97f8a)"></div><p>Pinot Rosé, La Castellana, Spumante Brut</p></article>
  <article class="abs card" style="left:498px"><div class="bottle" role="img" aria-label="Photo of a white wine bottle" style="background:linear-gradient(90deg,#55583a,#8c8e5e,#4a4c32)"></div><p>Peat San Martino della Battaglia, Fioravanti</p></article>
  <article class="abs card" style="left:700px"><div class="bottle" role="img" aria-label="Photo of a red wine bottle" style="background:linear-gradient(90deg,#1a1a1a,#3a3a3a,#151515)"></div><p>Brouilly, AP, Château des Rives</p></article>
  <article class="abs card" style="left:903px"><div class="bottle" role="img" aria-label="Photo of a Marsala wine bottle" style="background:linear-gradient(90deg,#8a4d20,#c98a4a,#7a4118)"></div><p>Marsala Superiore Secco, Borgonuovo</p></article>
</main>
</body>
</html>
```